School Communication Email Template

Looking for a designer to create a couple simple email templates that are matching our brand colors and feel. Attached is the default email template that is currently being sent out. Company details can be shared upon request.

Template is to be used within the booking tool we use (snapshot below) and gmail. Template code is in HTML (see screenshot below).
Updates

Template code for website should be in HTML. Sorry if that created confusion.

Target Market(s)

Parents of kids enrolled in our classes

Industry/Entity Type

Kids sport classes

Font styles to use
Serif

Colors
0054AA
0677BA
7BADD7
CADEEF
E8F1F8
FFF300
FFF600
FEFA6F
FFFEC7
FFFEE8

Requirements
Must have
• Consistency with company brand/colors
Nice to have
• Flexibility to be adjusted as needed

```html
<!DOCTYPE html>
<html lang="en">
<head>
<meta charset="UTF-8">
<title>Booking Confirmation</title>
<link rel="stylesheet" href="https://fonts.googleapis.com/css2?family=Montserrat:wght@400;500&display=swap">
<style>
  :root {
    --brand-blue: #213b94;
    --field-bg: #ffffff;
    --text-dark: #333333;
    --text-light: #ffffff;
    --page-bg: #ffffff;
  }
  * { box-sizing: border-box; margin: 0; padding: 0; }
  html, body {
    width: 1112px;
    height: 1200px;
    overflow: hidden;
    background: var(--page-bg);
    font-family: "Montserrat", sans-serif;
  }
  .email {
    position: relative;
    width: 1112px;
    height: 1200px;
    background: var(--page-bg);
  }
  .email-header {
    position: absolute;
    top: 0; left: 0;
    width: 1112px;
    height: 115px;
    display: flex;
    align-items: center;
    justify-content: center;
  }
  .brand-name {
    font-size: 26px;
    font-weight: 500;
    color: var(--brand-blue);
  }
  .email-body {
    position: absolute;
    top: 115px; left: 0;
    width: 1112px;
    height: 997px;
    background: var(--brand-blue);
    color: var(--text-light);
  }
  .label {
    position: absolute;
    left: 70px;
    font-size: 24px;
    font-weight: 400;
    line-height: 30px;
  }
  .greeting-label {
    top: 84px;
    font-weight: 500;
  }
  .section-title {
    position: absolute;
    left: 72px;
    top: 200px;
    font-size: 42px;
    font-weight: 400;
  }
  .field {
    position: absolute;
    height: 70px;
    background: var(--field-bg);
    color: var(--text-dark);
    font-size: 23px;
    line-height: 70px;
    padding-left: 44px;
    white-space: nowrap;
    box-shadow: 3px 4px 6px rgba(0, 0, 0, 0.3);
  }
  .field-greet-first { left: 161px; top: 70px; width: 356px; padding-left: 42px; }
  .field-greet-last  { left: 537px; top: 70px; width: 356px; padding-left: 42px; }
  .field-half-first  { left: 297px; width: 356px; }
  .field-half-last   { left: 673px; width: 356px; }
  .field-full        { left: 297px; width: 732px; }
  .email-footer {
    position: absolute;
    top: 1112px; left: 0;
    width: 1112px;
    height: 88px;
    display: flex;
    align-items: center;
    justify-content: center;
    font-size: 22px;
    color: var(--text-dark);
  }
</style>
</head>
<body>
  <main class="email">
    <header class="email-header">
      <span class="brand-name">Kelvra Juniors</span>
    </header>

    <section class="email-body">
      <span class="label greeting-label">Dear,</span>
      <div class="field field-greet-first">Jackson</div>
      <div class="field field-greet-last">Smith</div>

      <h1 class="section-title">Booking</h1>

      <span class="label" style="top:325px;">Student:</span>
      <div class="field field-half-first" style="top:305px;">Jane</div>
      <div class="field field-half-last" style="top:305px;">Smith</div>

      <span class="label" style="top:416px;">Appointment:</span>
      <div class="field field-full" style="top:395px;">Summer Camp</div>

      <span class="label" style="top:506px;">Service:</span>
      <div class="field field-full" style="top:485px;">Suimming</div>

      <span class="label" style="top:596px;">Start Date:</span>
      <div class="field field-full" style="top:576px;">15 Feb 2023</div>

      <span class="label" style="top:686px;">End Date:</span>
      <div class="field field-full" style="top:665px;">30 Mar 2023</div>

      <span class="label" style="top:776px;">Start Time:</span>
      <div class="field field-full" style="top:755px;">09:00 AM</div>

      <span class="label" style="top:866px;">End Time:</span>
      <div class="field field-full" style="top:845px;">12:30 PM</div>
    </section>

    <footer class="email-footer">2023 Copyrights. All Rights Reserved.</footer>
  </main>
</body>
</html>
```